Business car for dental practice

I have a new logo. Want it use for a new business card design. Hi end dental practice Would like a scan code on it for quick access to my web site and mobile site too. Green and purple are in logo design. Maybe have scan code on back? My website is peterhallwayDDS.example
Updates

Meadowlark Crest Dental Associates

482 N Tamarack Ln
Fernbrook, NY 10998
555-555-0173

367 W Corliss Dr. 
Suite 584
Harrow Glen, NY 10997
555-555-0198

would like to incorporate logo, and addresses of both offices, and I recently saw a business card with a scan box on it which would bring people directly to the web site. if anyone knows how to do that, that could possibly go on the back of the card. (May be something I have to add at printing process) card can be one sided, or two sided.  

Reason: designer is revising for me. has not posted changes yet. hope he does soon!!

```html
<!DOCTYPE html>
<html lang="en">
<head>
<meta charset="utf-8">
<title>Meadowlark Crest Dental Associates – Business Card</title>
<link rel="stylesheet" href="https://fonts.googleapis.com/css2?family=Arimo:wght@400&family=Tinos:wght@400;700&display=swap">
<style>
  :root {
    --plum: #5b2453;
    --leaf: #3fb04b;
    --paper: #ffffff;
    --edge: #3a2a36;
    --shadow: rgba(0,0,0,0.35);
  }
  html, body {
    margin: 0;
    padding: 0;
    width: 1200px;
    height: 1200px;
    overflow: hidden;
    background: var(--paper);
  }
  .canvas {
    position: relative;
    width: 1200px;
    height: 1200px;
  }
  .card {
    position: absolute;
    left: 364px;
    width: 468px;
    height: 284px;
    box-sizing: border-box;
    border: 1px solid var(--edge);
    background: var(--plum);
    box-shadow: 8px 8px 9px var(--shadow);
    overflow: hidden;
  }
  .card--front { top: 235px; }
  .card--back { top: 654px; }

  .front-header {
    position: absolute;
    left: 0; top: 0;
    width: 100%;
    height: 116px;
    background: var(--paper);
  }
  .brand {
    position: absolute;
    left: 22px;
    top: 21px;
    display: flex;
    align-items: center;
    gap: 8px;
  }
  .brand-mark {
    width: 34px;
    height: 34px;
    background: var(--leaf);
  }
  .brand-name {
    font-family: "Tinos", serif;
    font-weight: 400;
    font-size: 27px;
    color: var(--plum);
    line-height: 1;
  }
  .practice-name {
    position: absolute;
    left: 0; right: 0;
    top: 92px;
    margin: 0;
    text-align: center;
    font-family: "Tinos", serif;
    font-weight: 700;
    font-size: 19px;
    color: var(--leaf);
    line-height: 1;
  }
  .office {
    position: absolute;
    top: 226px;
    margin: 0;
    font-family: "Arimo", sans-serif;
    font-style: normal;
    font-size: 10.5px;
    letter-spacing: 0.9px;
    line-height: 12px;
    color: var(--leaf);
  }
  .office--first { left: 25px; text-align: left; }
  .office--second { right: 33px; text-align: right; }

  .website {
    position: absolute;
    left: 0; right: 0;
    top: 238px;
    margin: 0;
    text-align: center;
    font-family: "Arimo", sans-serif;
    font-size: 20px;
    letter-spacing: 2px;
    color: var(--leaf);
  }
</style>
</head>
<body>
<main class="canvas">
  <section class="card card--front" aria-label="Business card front">
    <div class="front-header">
      <div class="brand">
        <span class="brand-mark" aria-hidden="true"></span>
        <span class="brand-name">Meadowlark Crest</span>
      </div>
      <h1 class="practice-name">Meadowlark Crest Dental Associates</h1>
    </div>
    <address class="office office--first">
      482 N Tamarack Ln<br>
      Fernbrook, NY 10998<br>
      555-555-0173
    </address>
    <address class="office office--second">
      367 W Corliss Dr., Suite 584<br>
      Harrow Glen, NY 10997<br>
      555-555-0198
    </address>
  </section>

  <section class="card card--back" aria-label="Business card back">
    <p class="website">peterhallwayDDS.example</p>
  </section>
</main>
</body>
</html>
```